Personal contact Business card design needed

I work in the Property Industry - specifically Property Management.

I need a card I can hand out to colleagues at networking events, meetings, training courses etc. that will provide my contact details.

Target Market(s)

Professional colleagues / potential clients / employers

Industry/Entity Type

Training

Contact Information for Business Card

I need a simple and professional card to give to professional network contacts at meetings, interviews etc.

The card should include my photograph, name, mobile number, email address and Proflinx address.

I would like appropriate professional colours. Something feminine but not too 'frilly' or 'girly'

Requirements
Must have
• Photograph of myself.
I want it to be simple,perhaps a small icon for each contact detail such as
Email icon
Proflinx icon
Mobile number

```html
<!DOCTYPE html>
<html lang="en">
<head>
<meta charset="utf-8">
<title>Maria Dunn – Business Card</title>
<link rel="stylesheet" href="https://fonts.googleapis.com/css2?family=Indie+Flower&family=Quicksand:wght@400;600;700&display=swap">
<style>
  :root{
    --plum:#8b3270;
    --plum-dark:#2e2a2c;
    --paper:#f1f0ee;
    --ink:#3a3a3a;
    --ink-soft:#555;
    --stage:#6d6d6d;
    --white:#ffffff;
  }
  *{box-sizing:border-box;margin:0;padding:0}
  html,body{width:1200px;height:1000px;overflow:hidden}
  body{background:var(--stage);font-family:"Quicksand",sans-serif;position:relative}
  .card{position:absolute;left:300px;width:600px;height:404px;overflow:hidden;box-shadow:0 6px 18px rgba(0,0,0,.35)}
  .card--back{top:60px;background:var(--plum)}
  .card--front{top:520px;background:var(--paper)}
  .hand{font-family:"Indie Flower",cursive;font-variant-ligatures:none}

  .back-name{position:absolute;right:44px;bottom:22px;color:var(--white);font-size:64px;line-height:1}

  .label-name{position:absolute;left:24px;top:22px;font-weight:700;font-size:19px;color:var(--ink)}
  .full-name{position:absolute;left:24px;top:44px;font-size:30px;color:var(--plum)}
  .label-me{position:absolute;left:24px;top:118px;font-size:20px;color:var(--ink)}
  .photo{position:absolute;left:26px;top:152px;width:97px;height:111px;background:linear-gradient(160deg,#d9d3cc 0%,#8a7368 55%,#2a2224 100%)}
  .label-contact{position:absolute;left:284px;top:146px;font-size:20px;color:var(--ink)}
  .contact-band{position:absolute;left:280px;top:178px;width:320px;height:48px;background:var(--plum);border-left:7px solid var(--plum-dark);padding:5px 0 0 16px;color:var(--white);font-size:15px;line-height:19px}
  .contact-row{display:flex;align-items:center;gap:9px}
  .contact-row svg{flex:none}
  .label-profile{position:absolute;left:24px;top:282px;font-size:20px;color:var(--ink)}
  .profile-row{position:absolute;left:24px;top:336px;display:flex;align-items:center;gap:8px;font-size:14px;color:var(--ink-soft)}
  .profile-label{font-weight:400;color:var(--ink-soft)}
  .profile-url b{color:var(--ink);font-weight:700}
  .arrow{position:absolute;fill:none;stroke:var(--ink);stroke-width:2;stroke-linecap:round;stroke-linejoin:round}
  .wave{position:absolute;left:0;bottom:0}
</style>
</head>
<body>

<section class="card card--back" aria-label="Card back">
  <span class="back-name hand">Maria</span>
</section>

<section class="card card--front" aria-label="Card front">
  <span class="label-name">Name:</span>
  <svg class="arrow" style="left:92px;top:20px" width="34" height="30" viewBox="0 0 34 30"><path d="M4 6 C14 0 26 6 20 20"/><path d="M14 16 L20 22 L25 14"/></svg>
  <span class="full-name hand">Maria Dunn</span>

  <span class="label-me hand">This is me:</span>
  <svg class="arrow" style="left:120px;top:118px" width="44" height="44" viewBox="0 0 44 44"><path d="M6 4 C30 2 40 24 22 34"/><path d="M28 38 L20 35 L24 27"/></svg>
  <div class="photo" role="img" aria-label="Portrait photograph of the card owner"></div>

  <span class="label-contact hand">contact me</span>
  <div class="contact-band">
    <div class="contact-row">
      <svg width="14" height="12" viewBox="0 0 14 12"><path fill="#fff" d="M1 4 C1 1 13 1 13 4 L11 5 L10 3.5 L4 3.5 L3 5 Z M3 6 L11 6 L12 11 L2 11 Z"/></svg>
      <span>0400 555 123</span>
    </div>
    <div class="contact-row">
      <svg width="14" height="10" viewBox="0 0 14 10"><rect x="0.5" y="0.5" width="13" height="9" fill="#fff"/><path d="M0.5 0.5 L7 6 L13.5 0.5" fill="none" stroke="#8b3270"/></svg>
      <span>maria@mailbox-example.com.au</span>
    </div>
  </div>

  <span class="label-profile hand">And this is my proflinx profile</span>
  <svg class="arrow" style="left:300px;top:284px" width="60" height="60" viewBox="0 0 60 60"><path d="M8 6 C46 2 58 34 20 48"/><path d="M28 54 L18 48 L26 40"/></svg>
  <div class="profile-row">
    <span class="profile-label">Proflinx</span>
    <span class="profile-url">proflinx-example.net/<b>maria-dunn</b></span>
  </div>

  <svg class="wave" width="600" height="44" viewBox="0 0 600 44"><path d="M0 14 L300 26 L600 2 L600 44 L0 44 Z" fill="var(--plum)"/></svg>
</section>

</body>
</html>
```